Poultry Animal Health Product Label Design for Backyard Farmers

We need a label design for a new brand (name to be finalized yet - will use ClearHarbor logo attached as a placeholder). We will launch several products for backyard farmers to use on their chickens. These products will treat insect and parasite problems on chickens and their coops. Products will be sold in farm & fleet stores and packaged in a powder bottle (similar to baby powder with shaker top - attached to project with a Tolbrine label on it currently for a different brand/product - should be replaced with proposed design) and aerosol cans. Designs should consider photographic or illustration treatment, incorporation of imagery of farms or chickens, use of bold, bright colors (prefer NOT to use yellow as a competitor brand already uses soft yellow primarily). Design needs to work across 2 different package formats: powder bottle and aerosol.

Product in shaker needs to have this copy on the front (aerosols will be similar in amount and type of copy required - specifics not yet defined):
- ClearHarbor logo
- Poultry Dust
- Controls Northern Fowl Mite, Lice
- Nature-derived active ingredients are safe for use around people and animals
- Ingredients (will be provided for final design, not yet public)

Brainstorming to date that we liked includes landscape imagery, bright/bold images of chickens, potentially more playful integration of chickens (either caricature or photographic with speech bubbles announcing product use like, "Help! I've got mites!"), and potential inclusion of person (should be female or child - could be just arms holding a chicken rather than full body).

Target Market(s)

Consumers with backyard chickens - typically raised as pets for daily eggs

Industry/Entity Type

Health Product

Requirements
Must have
• Design shown as a label on the powder bottle attached
Nice to have
• Extend design to a standard aerosol can to show portfolio look. Does NOT have to be identical across products - could use different chicken images, for instance.
Should not have
• Yellow cannot be the primary or dominant color as several competitors use yellow almost exclusively.

```html
<!DOCTYPE html>
<html lang="en">
<head>
<meta charset="utf-8">
<title>Poultry Label Designs</title>
<link rel="stylesheet" href="https://fonts.googleapis.com/css2?family=Comfortaa:wght@500&family=Open+Sans:wght@400;700&family=Michroma&family=Roboto+Condensed:wght@400;500&display=swap">
<style>
  :root {
    --page: #ffffff;
    --card-edge: #8a8a8a;
    --frame: #2b2d8c;
    --brand-green: #7cbc42;
    --brand-navy: #2e3192;
    --alert-red: #ed1c24;
    --claim-green: #8dc63f;
    --bubble: #2b3a8f;
    --ink: #111111;
    --seal-blue: #1c75bc;
    --logo-green: #2aa344;
  }
  * { margin: 0; padding: 0; box-sizing: border-box; }
  html, body { width: 1200px; height: 1000px; overflow: hidden; background: var(--page); }
  .canvas { position: relative; width: 1200px; height: 1000px; }

  .label-card {
    position: absolute; top: 87px; width: 424px; height: 812px;
    border: 1px solid var(--card-edge); background: var(--page);
  }
  .label-card--dust { left: 155px; }
  .label-card--spray { left: 619px; height: 810px; }

  .label-frame {
    position: absolute; left: 18px; top: 18px; width: 387px; height: 776px;
    border: 1.5px solid var(--frame);
    border-radius: 18px / 50px;
    overflow: hidden;
  }

  .brand-name {
    position: absolute; left: 0; right: 0; top: 42px;
    text-align: center; font-family: "Comfortaa", sans-serif; font-weight: 500;
    font-size: 48px; letter-spacing: -1.5px; line-height: 1; white-space: nowrap;
  }
  .label-card--dust .brand-name { color: var(--brand-green); }
  .label-card--spray .brand-name { color: var(--brand-navy); }

  .product-type {
    position: absolute; left: 0; right: 0; top: 112px;
    text-align: center; font-family: "Open Sans", sans-serif;
    font-size: 36px; color: var(--ink); line-height: 1; white-space: nowrap;
  }

  .claim-band {
    position: absolute; left: 0; right: 0; top: 175px; height: 117px;
    background: var(--alert-red); color: #fff; text-align: center;
    font-family: "Michroma", sans-serif; line-height: 1; white-space: nowrap;
  }
  .claim-band .claim-lead { display: block; font-size: 33px; margin-top: 7px; letter-spacing: 3px; }
  .claim-band .claim-target { display: block; font-size: 26px; margin-top: 6px; letter-spacing: 3px; }

  .scene { position: absolute; border-radius: 6px; }
  .label-card--dust .scene {
    left: 66px; top: 318px; width: 300px; height: 200px;
    background: radial-gradient(ellipse at 60% 45%, #e9b99a 0%, #f3e06a 55%, #ffffff 85%);
  }
  .label-card--spray .scene {
    left: 140px; top: 328px; width: 240px; height: 190px;
    background: radial-gradient(ellipse at 50% 55%, #d8d8d8 0%, #eeeeee 50%, #ffffff 85%);
  }

  .speech-bubble {
    position: absolute; background: var(--bubble); color: #fff;
    border-radius: 5px; text-align: center;
    font-family: "Roboto Condensed", sans-serif; font-size: 19px; line-height: 1.3;
    padding-top: 8px; white-space: nowrap;
  }
  .speech-tail { position: absolute; }
  .label-card--dust .speech-bubble { left: 10px; top: 305px; width: 118px; height: 78px; font-size: 20px; }
  .label-card--dust .speech-tail { left: 73px; top: 382px; }
  .label-card--spray .speech-bubble { left: 6px; top: 296px; width: 119px; height: 133px; font-size: 17px; line-height: 1.35; }
  .label-card--spray .speech-tail { left: 124px; top: 368px; }

  .safety-band {
    position: absolute; left: 0; right: 0; top: 519px; height: 84px;
    background: var(--claim-green); color: var(--ink); text-align: center;
    font-family: "Roboto Condensed", sans-serif; font-weight: 500;
    font-size: 22px; letter-spacing: -0.3px; line-height: 34px;
    padding-top: 8px; white-space: nowrap; overflow: hidden;
  }
  .label-card--spray .safety-band { top: 522px; }

  .seal { position: absolute; left: 28px; top: 613px; width: 98px; height: 98px; }
  .label-card--spray .seal { left: 26px; top: 612px; }

  .ingredients {
    position: absolute; left: 150px; top: 607px; width: 220px;
    text-align: center; font-family: "Michroma", sans-serif; color: var(--ink);
  }
  .ingredients h2 { font-size: 17px; font-weight: 400; letter-spacing: 2px; line-height: 1.2; }
  .ingredients li { list-style: none; font-size: 16px; letter-spacing: 2px; line-height: 25px; }
  .label-card--spray .ingredients { left: 155px; top: 609px; }

  .company-name {
    position: absolute; left: 0; right: 0; top: 717px; text-align: center;
    font-family: "Open Sans", sans-serif; font-weight: 700; font-size: 34px;
    color: var(--logo-green); line-height: 1;
  }
  .label-card--spray .company-name { top: 713px; }
</style>
</head>
<body>
<main class="canvas">

  <section class="label-card label-card--dust">
    <div class="label-frame">
      <h1 class="brand-name">Brand Name</h1>
      <p class="product-type">Poultry Dust</p>
      <div class="claim-band">
        <span class="claim-lead">Controls</span>
        <span class="claim-target">Northern Fowl</span>
        <span class="claim-target">Mite &amp; Lice</span>
      </div>
      <div class="scene" role="img" aria-label="Cartoon hen with three yellow chicks"></div>
      <p class="speech-bubble">Mommy, Help!<br>I've got mites!</p>
      <svg class="speech-tail" width="16" height="20" viewBox="0 0 16 20"><path d="M0 0 H16 L10 20 Z" fill="#2b3a8f"/></svg>
      <p class="safety-band">Nature-derived active ingredients<br>are safe for use around people and animals</p>
      <svg class="seal" viewBox="0 0 100 100" role="img" aria-label="Certification seal">
        <circle cx="50" cy="50" r="48" fill="#1c75bc"/>
        <circle cx="50" cy="50" r="34" fill="#111"/>
        <circle cx="50" cy="50" r="27" fill="#1c75bc"/>
      </svg>
      <div class="ingredients">
        <h2>Ingredients</h2>
        <ul><li>xxxxxx</li><li>xxxxxx</li><li>xxxxxx</li></ul>
      </div>
      <p class="company-name">ClearHarbor</p>
    </div>
  </section>

  <section class="label-card label-card--spray">
    <div class="label-frame">
      <h1 class="brand-name">Brand Name</h1>
      <p class="product-type">Poultry Spray</p>
      <div class="claim-band">
        <span class="claim-lead">Controls</span>
        <span class="claim-target">Northern Fowl</span>
        <span class="claim-target">Mite &amp; Lice</span>
      </div>
      <div class="scene" role="img" aria-label="Illustrated rooster crowing at a white hen"></div>
      <p class="speech-bubble">Wow!<br>You're so pretty.<br>Ohhhh...<br>You've mites!</p>
      <svg class="speech-tail" width="24" height="18" viewBox="0 0 24 18"><path d="M0 0 L24 9 L0 18 Z" fill="#2b3a8f"/></svg>
      <p class="safety-band">Nature-derived active ingredients<br>are safe for use around people and animals</p>
      <svg class="seal" viewBox="0 0 100 100" role="img" aria-label="Certification seal">
        <circle cx="50" cy="50" r="48" fill="#1c75bc"/>
        <circle cx="50" cy="50" r="34" fill="#111"/>
        <circle cx="50" cy="50" r="27" fill="#1c75bc"/>
      </svg>
      <div class="ingredients">
        <h2>Ingredients</h2>
        <ul><li>xxxxxx</li><li>xxxxxx</li><li>xxxxxx</li></ul>
      </div>
      <p class="company-name">ClearHarbor</p>
    </div>
  </section>

</main>
</body>
</html>
```